Course Syllabus Template for LMG

We need a nice course syllabus created. The first page should be a cover page that includes our logo, website, and a nice picture of of a K12 teacher working with students. We've uploaded an example that artists can use if needed. The subsequent pages should just have header/footer saved that look nice and consistent throughout the rest of the document. On the subsequent pages, they don't need to have too much design but should include our website and potentially our logo or color scheme.

Additionally, we've attached a current syllabus so you can see what our current product is. In the syllabus, we have a spacer that separates the different sections of the syllabus. Ideally, we'd like a couple design options that we could use as spacers instead of the large green block that we currently use.

Full list of Items:
- Cover page (including logo, website & photo)
- template header/footer for subsequent pages that includes website, potentially logo and color scheme.
- Spacer to divide the sections of the syllabus.
- File must be in word.doc format

*We attached a PDF of a competitors syllabus that we like and thought would be a good point of reference.

Company Website is www.brightlanelearning.example.

Once completed, we would enter in all the text that is necessary for each specific course onto the syllabus template.

Target Market(s)

K12 Educators & Teachers

Colors

Designer to choose colors to be used in the design.

Requirements
Must have
• Items listed in Project dsign

```html
<!DOCTYPE html>
<html lang="en">
<head>
<meta charset="utf-8">
<title>LMG Course Syllabus Cover</title>
<link rel="stylesheet" href="https://fonts.googleapis.com/css2?family=Anton&family=Oswald:wght@600&family=Roboto:wght@500&display=swap">
<style>
  :root {
    --backdrop: #b4b4b4;
    --paper: #ffffff;
    --tint: #e6f0d6;
    --green: #6cbf2c;
    --green-deep: #4f9a1f;
    --charcoal: #3a3a3a;
    --ink: #2b2b2b;
    --photo-warm: #c9a98e;
    --photo-cool: #9fb4c8;
  }
  * { box-sizing: border-box; margin: 0; padding: 0; }
  html, body { width: 1200px; height: 800px; overflow: hidden; }
  body { background: var(--backdrop); position: relative; }

  .cover {
    position: absolute;
    left: 310px; top: 25px;
    width: 580px; height: 750px;
    background: linear-gradient(160deg, var(--tint) 0%, var(--paper) 55%, var(--tint) 100%);
    overflow: hidden;
    box-shadow: 0 6px 24px rgba(0,0,0,.25);
  }
  .cover__shapes { position: absolute; inset: 0; }

  .brand {
    position: absolute;
    top: 60px; left: 0; right: 0;
    display: flex; align-items: center; justify-content: center; gap: 16px;
  }
  .brand__dot {
    width: 58px; height: 58px; border-radius: 50%;
    background: var(--green);
  }
  .brand__name {
    font-family: "Oswald", sans-serif;
    font-weight: 600;
    font-size: 60px;
    line-height: 1;
    letter-spacing: 2px;
    color: var(--green);
  }

  .cover__photo {
    position: absolute;
    left: 0; top: 172px;
    width: 580px; height: 350px;
    background: linear-gradient(120deg, var(--photo-cool) 0%, #e9e3dc 35%, var(--photo-warm) 70%, #8a6a58 100%);
    clip-path: polygon(0 0, 100% 0, 100% 100%, 0 77%);
  }

  .title {
    position: absolute;
    left: 115px; top: 540px;
    display: grid;
    grid-template-columns: auto auto;
    align-items: end;
    font-family: "Anton", sans-serif;
    text-transform: uppercase;
    line-height: .9;
  }
  .title__initial {
    grid-row: 1 / span 2;
    font-size: 132px;
    color: var(--green);
    line-height: .82;
  }
  .title__top { font-size: 50px; color: var(--charcoal); letter-spacing: 1px; }
  .title__rest { font-size: 58px; color: var(--green); }
  .title__tail {
    grid-column: 1 / span 2;
    font-size: 36px;
    color: var(--charcoal);
    margin-top: 4px;
  }
  .website {
    position: absolute;
    left: 95px; top: 700px; width: 360px;
    display: flex; align-items: center; gap: 10px;
    font-family: "Roboto", sans-serif;
    font-weight: 500;
    font-size: 14px;
    color: var(--ink);
  }
  .website::before, .website::after {
    content: ""; flex: 1; height: 2px; background: var(--charcoal);
  }
</style>
</head>
<body>
  <section class="cover">
    <svg class="cover__shapes" width="580" height="750" viewBox="0 0 580 750" aria-hidden="true">
      <polygon points="0,0 190,0 0,40" fill="var(--green)"/>
      <polygon points="200,0 580,0 580,14 230,14" fill="var(--charcoal)"/>
      <polygon points="300,24 580,24 580,40 330,40" fill="var(--green)"/>
      <rect x="0" y="166" width="580" height="5" fill="var(--charcoal)"/>
      <polygon points="0,441 580,522 580,528 0,447" fill="var(--charcoal)"/>
      <polygon points="0,660 240,750 0,750" fill="var(--green)"/>
      <polygon points="240,750 0,660 0,650 270,750" fill="var(--charcoal)"/>
      <polygon points="420,750 580,690 580,750" fill="var(--charcoal)"/>
      <polygon points="470,750 580,712 580,750" fill="var(--green)"/>
    </svg>

    <div class="brand">
      <span class="brand__dot"></span>
      <span class="brand__name">LMG</span>
    </div>

    <div class="cover__photo" role="img" aria-label="Photo of a smiling teacher helping two young students with their classwork at a desk"></div>

    <h1 class="title">
      <span class="title__initial">M</span>
      <span class="title__top">Growth</span>
      <span class="title__rest">indset</span>
      <span class="title__tail">In the Classroom</span>
    </h1>
    <p class="website">www.brightlanelearning.example</p>
  </section>
</body>
</html>
```